Business Card Design Project

Use our current logo. Clean design.

Industry/Entity Type

Business

Requirements
Must have
• Marisela DUBRANCQ
M. Law
Managing Partner

Alpenvorsa AG
Kornhalmweg 214
CH-3097 Liebefeld

M. +41 79 412 56 27
T. +41 31 928 44 10
F. +41 31 928 44 19

m.dubrancq@alpenvorsa-example.com
www.alpenvorsa-example.com

```html
<!DOCTYPE html>
<html lang="en">
<head>
<meta charset="utf-8">
<title>Alpenvorsa AG – Business Card</title>
<link href="https://fonts.googleapis.com/css2?family=Arimo:wght@400;700&display=swap" rel="stylesheet">
<style>
  :root {
    --gold: #f2a81c;
    --gold-deep: #c98600;
    --gold-light: #ffcf45;
    --ink: #111111;
    --paper: #ffffff;
    --grey: #8a8a8a;
    --canvas: #ffffff;
  }
  * { box-sizing: border-box; margin: 0; padding: 0; }
  html, body {
    width: 1200px; height: 352px; overflow: hidden;
    background: var(--canvas);
    font-family: "Arimo", Arial, sans-serif;
  }
  .sheet { position: relative; width: 1200px; height: 352px; }
  .card {
    position: absolute; top: 20px; width: 576px; height: 312px; overflow: hidden;
  }

  /* Front */
  .card--front {
    left: 12px; background: var(--paper);
    border: 1px solid #d9d9d9;
  }
  .top-bar {
    position: absolute; left: 0; top: 30px; width: 270px; height: 40px;
    background: var(--ink);
  }
  .top-rule {
    position: absolute; left: 270px; top: 68px; right: 0; height: 2px;
    background: linear-gradient(to right, var(--ink), #cfcfcf);
  }
  .identity { position: absolute; left: 300px; top: 28px; }
  .identity__name {
    color: var(--gold); font-weight: 700; font-size: 16px; letter-spacing: 1.5px;
    text-transform: uppercase;
  }
  .identity__degree {
    color: var(--ink); font-size: 9px; font-weight: 700; letter-spacing: 0; text-transform: none;
  }
  .identity__role { color: var(--ink); font-size: 12px; margin-top: 6px; }
  .address {
    position: absolute; left: 300px; top: 124px;
    font-size: 11.5px; line-height: 15px; color: var(--ink); font-style: normal;
  }
  .contacts { position: absolute; left: 292px; top: 164px; right: 0; list-style: none; }
  .contact {
    display: flex; align-items: center; height: 32px; margin-bottom: 4px;
    background: var(--ink); color: var(--paper); font-size: 11.5px; letter-spacing: .3px;
  }
  .contact__icon {
    width: 22px; height: 22px; margin: 0 22px 0 8px; flex: none;
  }
  .brand { position: absolute; left: 34px; top: 222px; width: 210px; text-align: center; }
  .brand__name {
    font-weight: 700; font-size: 28px; letter-spacing: 1px; color: var(--ink);
  }
  .brand__web { margin-top: 14px; color: var(--gold); font-size: 14px; font-weight: 700; }

  /* Back */
  .card--back {
    left: 612px;
    background: radial-gradient(ellipse at 50% 40%, var(--gold-light) 0%, var(--gold) 45%, var(--gold-deep) 100%);
  }
  .back-brand {
    position: absolute; top: 100px; left: 0; right: 0; text-align: center;
    color: var(--paper); font-weight: 700; font-size: 36px; letter-spacing: 2px;
  }
  .back-band {
    position: absolute; left: 0; right: 0; top: 196px; height: 56px;
    background: linear-gradient(to right, #4a4a4a 0%, var(--ink) 18%, var(--ink) 82%, #4a4a4a 100%);
    display: flex; align-items: center; justify-content: center;
    color: var(--paper); font-weight: 700; font-size: 27px;
  }
</style>
</head>
<body>
<div class="sheet">

  <section class="card card--front">
    <div class="top-bar"></div>
    <div class="top-rule"></div>

    <div class="identity">
      <p class="identity__name">Marisela Dubrancq <span class="identity__degree">(M. Law)</span></p>
      <p class="identity__role">Managing Partner</p>
    </div>

    <address class="address">
      Alpenvorsa AG, Kornhalmweg 214<br>
      CH-3097 Liebefeld
    </address>

    <ul class="contacts">
      <li class="contact">
        <svg class="contact__icon" viewBox="0 0 22 22"><rect x="1" y="1" width="20" height="20" fill="none" stroke="#fff" stroke-width="1.2"/><rect x="7.5" y="4.5" width="7" height="13" rx="1" fill="none" stroke="#fff" stroke-width="1.4"/><circle cx="11" cy="15.3" r=".9" fill="#fff"/></svg>
        +41 79 412 56 27
      </li>
      <li class="contact">
        <svg class="contact__icon" viewBox="0 0 22 22"><rect x="1" y="1" width="20" height="20" fill="none" stroke="#fff" stroke-width="1.2"/><path d="M5 9 Q11 4 17 9 L15.5 11 L13.5 10 L13.5 8.5 Q11 7.6 8.5 8.5 L8.5 10 L6.5 11 Z" fill="#fff"/><rect x="6.5" y="12" width="9" height="5" fill="#fff"/></svg>
        +41 31 928 44 10
      </li>
      <li class="contact">
        <svg class="contact__icon" viewBox="0 0 22 22"><rect x="1" y="1" width="20" height="20" fill="none" stroke="#fff" stroke-width="1.2"/><rect x="7" y="4.5" width="8" height="5" fill="none" stroke="#fff" stroke-width="1.2"/><rect x="5" y="9.5" width="12" height="7" fill="#fff"/></svg>
        +41 31 928 44 19
      </li>
      <li class="contact">
        <svg class="contact__icon" viewBox="0 0 22 22"><rect x="1" y="1" width="20" height="20" fill="none" stroke="#fff" stroke-width="1.2"/><rect x="5" y="7" width="12" height="8" fill="none" stroke="#fff" stroke-width="1.3"/><path d="M5 7 L11 12 L17 7" fill="none" stroke="#fff" stroke-width="1.3"/></svg>
        m.dubrancq@alpenvorsa-example.com
      </li>
    </ul>

    <div class="brand">
      <p class="brand__name">ALPENVORSA</p>
      <p class="brand__web">www.alpenvorsa-example.com</p>
    </div>
  </section>

  <section class="card card--back">
    <p class="back-brand">ALPENVORSA</p>
    <div class="back-band">www.alpenvorsa-example.com</div>
  </section>

</div>
</body>
</html>
```